Geschäftspapiere für Spezialist für Fliesen, Kaminöfen etc.
Zielgruppe
Wir sind ein Familienunternehmen in dritter Generation und Spezialist für Fliesen, Natursteine, Kaminöfen, Schwimmbäder und Whirlpools. Professionell, kreativ und voller Leidenschaft begleiten wir unsere Kunden bei der Umsetzung ihrer Vorhaben. Von der persönlichen Beratung bis hin zur Ausführung profitieren unsere Kunden von qualifiziertem Fachpersonal und 60 Jahren Erfahrung. Unsere Zielgruppe sind Familien/Paare ab 35 Jahren, die hochwertige Produkte für Ihr Zuhause suchen.
Aufgabenstellung
Wir benötigen neues Briefpapier, da wir ein neues Logo haben. Wir hätten gerne drei bis vier Bilder in der Kopfleiste. Des weiteren soll unser Portfolio aufgelistet sein (Fliesen, Natursteine, Kaminöfen, Schwimmbäder und Whirlpools). Das Logo soll in weiß gedruckt werden, der Hintergrund sollte daher dunkel sein (Farbton ähnlich DB703). Wir haben bereits selbst einen Entwurf gestaltet, in welche Richtung das Design gehen soll, sind jedoch offen für Ideen und Vorschläge.
Schriftart: z. B. Syncopate in Großbuchstaben

```html
<!DOCTYPE html>
<html lang="de">
<head>
<meta charset="utf-8">
<title>Briefbogen Naturstein-Merk</title>
<link rel="stylesheet" href="https://fonts.googleapis.com/css2?family=Figtree:wght@300;400&family=Montserrat:wght@500&display=swap">
<style>
  :root {
    --backdrop: #d2c8c9;
    --paper: #ffffff;
    --band: #4a4646;
    --ink: #3d3a3a;
    --footer-bg: #dcdadb;
    --fold: #9a9696;
    --photo-living: linear-gradient(135deg, #d9c7ad, #efe6da 55%, #8b6a4c);
    --photo-bath: linear-gradient(135deg, #e8e8e8, #f6f6f6 50%, #b9b6b2);
    --photo-stove: linear-gradient(135deg, #6f8a5a, #c9bfb3 45%, #b8453a);
    --photo-pool: linear-gradient(180deg, #d9e6ef, #c9c9c4 45%, #6fa64a 70%, #64c9e6);
  }
  * { box-sizing: border-box; margin: 0; padding: 0; }
  html, body { width: 960px; height: 1200px; overflow: hidden; background: var(--backdrop); }
  body { font-family: "Figtree", sans-serif; font-weight: 300; color: var(--ink); }

  .letter {
    position: absolute; left: 83px; top: 38px;
    width: 794px; height: 1122px;
    background: var(--paper);
  }

  .header-photos { position: absolute; left: 0; top: 0; width: 794px; height: 107px; display: flex; }
  .header-photos div { height: 100%; }
  .photo-living { width: 195px; background: var(--photo-living); }
  .photo-bath { width: 200px; background: var(--photo-bath); }
  .photo-stove { width: 200px; background: var(--photo-stove); }
  .photo-pool { width: 199px; background: var(--photo-pool); }

  .portfolio-band {
    position: absolute; left: 0; top: 107px; width: 794px; height: 28px;
    background: var(--band);
  }
  .portfolio {
    position: absolute; left: 48px; top: 0; width: 514px; height: 28px;
    display: flex; justify-content: space-between; align-items: center;
    list-style: none;
    font-family: "Montserrat", sans-serif; font-weight: 500;
    font-size: 10px; letter-spacing: 0.22em; color: #fff;
  }

  .brand-name {
    position: absolute; left: 600px; top: 0; height: 28px;
    display: flex; align-items: center; gap: 8px;
    font-family: "Figtree", sans-serif; font-weight: 400;
    font-size: 15px; color: #fff;
  }
  .brand-name .mark { width: 9px; height: 9px; background: #fff; }

  .sender-line {
    position: absolute; left: 96px; top: 188px;
    font-size: 11.5px; font-weight: 400;
  }

  .contact {
    position: absolute; left: 595px; top: 184px;
    font-size: 12.5px; line-height: 16px; font-weight: 300; font-style: normal;
  }
  .contact p + p { margin-top: 16px; }

  .fold-mark { position: absolute; left: 0; width: 13px; height: 0; border-top: 1px solid var(--fold); }
  .fold-mark.top { top: 397px; opacity: .5; }
  .fold-mark.punch { top: 559px; border-color: var(--ink); }
  .fold-mark.bottom { top: 794px; opacity: .5; }

  .footer {
    position: absolute; left: 0; top: 1021px; width: 794px; height: 101px;
    background: var(--footer-bg);
    font-size: 12px; line-height: 16px;
  }
  .footer-col { position: absolute; top: 13px; }
  .footer-col.bank { left: 95px; }
  .footer-col.management { left: 458px; }
  .footer-col.register { left: 595px; }
</style>
</head>
<body>
  <main class="letter">
    <div class="header-photos">
      <div class="photo-living" role="img" aria-label="Heller Wohnraum mit Natursteinwand und Kamin"></div>
      <div class="photo-bath" role="img" aria-label="Modernes Bad mit Marmorfliesen und freistehender Wanne"></div>
      <div class="photo-stove" role="img" aria-label="Wohnzimmer mit Kaminofen vor Natursteinwand"></div>
      <div class="photo-pool" role="img" aria-label="Moderne Villa mit Schwimmbecken im Garten"></div>
    </div>

    <div class="portfolio-band">
      <ul class="portfolio">
        <li>FLIESEN</li>
        <li>NATURSTEINE</li>
        <li>KAMINÖFEN</li>
        <li>SCHWIMMBÄDER</li>
        <li>WHIRLPOOLS</li>
      </ul>
      <div class="brand-name"><span class="mark"></span>Naturstein-Merk</div>
    </div>

    <p class="sender-line">Naturstein-Merk GmbH · Lindenauer Weg 12 · 67459 Talheim</p>

    <address class="contact">
      <p>Naturstein-Merk GmbH<br>Lindenauer Weg 12<br>67459 Talheim</p>
      <p>Tel.: 0 62 14-38 27 00<br>kontakt@naturstein-merk.de<br>www.naturstein-merk.de</p>
      <p>Mo–Fr 8:00–18:00 Uhr<br>Sa 8:00–13:00 Uhr</p>
    </address>

    <span class="fold-mark top"></span>
    <span class="fold-mark punch"></span>
    <span class="fold-mark bottom"></span>

    <footer class="footer">
      <div class="footer-col bank">
        Kreissparkasse Talheim<br>
        IBAN: DE00 1234 5678 0000 1122 33<br>
        Volksbank Rebenland eG<br>
        IBAN: DE00 8765 4321 0009 8877 66
      </div>
      <div class="footer-col management">
        Geschäftsführer:<br>
        Reinhard Merk<br>
        Tobias Merk<br>
        Lorenzo Merk
      </div>
      <div class="footer-col register">
        Amtsgericht Talheim<br>
        HRB 2741<br>
        USt-IdNr. DE000111222<br>
        St-Nr. 00/123/4567/8
      </div>
    </footer>
  </main>
</body>
</html>
```